A hand soap seller needs a premium label for a new product

We need a premium label for a bottle of soap. We want to write on it:
TAVRELMIK (Name)
Hypoallergenic and antibacterial hand soap
350 ml e / 11.8 fl oz (volume, http://pramvel.ru/7Q2KsNbwTre845)
Saint Petersburg - Russia / www.tavrelmik.ru
We want to see the face of a hippopotamus in the design. Use only black and white and green for accents (the color of grass). Examples of a hippopotamus are shown in the photo. Our soap is hypoallergenic. Ideal for both children and adults. Therefore, the label should appeal to adults and children.
The bottle will be white, and the soap dispenser will be black.
So I'm attaching an example of a soap design that we liked
Label size: height-78 mm, width-102 mm !!!

Target Market(s)

Mothers and children

Industry/Entity Type

Hand soap

Font styles to use
Serif

Colors

Designer to choose only greyscale colors for use in the design.

Requirements
Must have
• The face of a hippopotamus emerging from the grass, Black and white palette with elements of green (grass color)
Nice to have
• The face of a hippopotamus emerging from the grass
Should not have
• Different colors

```html
<!DOCTYPE html>
<html lang="en">
<head>
<meta charset="utf-8">
<title>TAVRELMIK Hypoallergenic Hand Soap Label</title>
<link rel="stylesheet" href="https://fonts.googleapis.com/css2?family=Sniglet:wght@800&family=Quicksand:wght@500&family=Montserrat:wght@300;400&family=Open+Sans:wght@700&display=swap">
<style>
  :root {
    --backdrop: #8f8f8f;
    --label: #ffffff;
    --accent: #6bb399;
    --accent-soft: #afdfcf;
    --ink-grey: #555555;
  }
  html, body {
    margin: 0;
    padding: 0;
    width: 918px;
    height: 1200px;
    overflow: hidden;
    background: var(--backdrop);
  }
  .canvas {
    position: relative;
    width: 918px;
    height: 1200px;
  }
  .label {
    position: absolute;
    left: 98px;
    top: 128px;
    width: 722px;
    height: 945px;
    background: var(--label);
    border-radius: 284px / 287px;
    box-shadow: 0 0 14px rgba(0, 0, 0, 0.35);
  }
  .brand-arc {
    position: absolute;
    left: 0;
    top: 0;
    width: 918px;
    height: 1200px;
    pointer-events: none;
  }
  .brand-arc text {
    font-family: "Sniglet", "Comic Sans MS", sans-serif;
    font-weight: 800;
    font-size: 60px;
    fill: var(--accent);
    letter-spacing: 10px;
  }
  .mascot-area {
    position: absolute;
    left: 324px;
    top: 314px;
    width: 271px;
    height: 323px;
    border-radius: 40% 40% 46% 46%;
    background: linear-gradient(180deg, var(--accent) 0%, var(--accent) 42%, var(--accent-soft) 44%, var(--accent-soft) 86%, var(--accent) 88%);
  }
  .product-name {
    position: absolute;
    left: 0;
    top: 670px;
    width: 918px;
    height: 60px;
  }
  .product-name text {
    font-family: "Quicksand", "Arial", sans-serif;
    font-weight: 500;
    font-size: 60px;
    fill: var(--accent);
  }
  .product-type {
    position: absolute;
    left: 0;
    width: 918px;
    top: 747px;
    margin: 0;
    text-align: center;
    font-family: "Montserrat", "Arial", sans-serif;
    font-weight: 400;
    font-size: 28px;
    letter-spacing: 19px;
    text-indent: 19px;
    color: var(--ink-grey);
  }
  .volume {
    position: absolute;
    left: 0;
    width: 918px;
    top: 868px;
    margin: 0;
    text-align: center;
    font-family: "Open Sans", "Arial", sans-serif;
    font-weight: 700;
    font-size: 29px;
    letter-spacing: 4px;
    color: var(--accent);
  }
  .origin {
    position: absolute;
    left: 0;
    width: 918px;
    top: 972px;
    margin: 0;
    text-align: center;
    font-family: "Montserrat", "Arial", sans-serif;
    font-weight: 300;
    font-size: 24px;
    line-height: 33px;
    letter-spacing: 3px;
    color: var(--ink-grey);
  }
</style>
</head>
<body>
  <main class="canvas">
    <div class="label"></div>

    <svg class="brand-arc" viewBox="0 0 918 1200" aria-label="TAVRELMIK">
      <defs>
        <path id="brand-curve" d="M 200 306 A 391 391 0 0 1 718 306" fill="none"/>
      </defs>
      <text><textPath href="#brand-curve" startOffset="50%" text-anchor="middle">TAVRELMIK</textPath></text>
    </svg>

    <div class="mascot-area" role="img" aria-label="Illustration of a friendly cartoon hippopotamus head in green tones"></div>

    <svg class="product-name" viewBox="0 0 918 60">
      <text x="137" y="52" textLength="644" lengthAdjust="spacing">HYPOALLERGENIC</text>
    </svg>

    <p class="product-type">HAND SOAP</p>

    <p class="volume">350 ml e / 11.8 fl oz</p>

    <p class="origin">Saint Petersburg - Russia<br>www.tavrelmik.ru</p>
  </main>
</body>
</html>
```